Lose Up To 1 LB Of Fat Per Day

We need a double sided street sign for our weight loss clinic. We need the doctors picture to the right side of the sign and we need a challenge “Lose Up To 1 Pound Of Fat Per Day” included in the signage.
Our color scheme for the clinic are black, white, teal and silver.
The phone number should be at the bottom of the sign
555-206–3948

Target Market(s)

Weight Loss

Font styles to use
Sans Serif

```html
<!DOCTYPE html>
<html lang="en">
<head>
<meta charset="UTF-8">
<title>Dr. Halvorsen's Weight Loss Program – Street Sign</title>
<link href="https://fonts.googleapis.com/css2?family=Fredoka:wght@600;700&family=Raleway:wght@400&display=swap" rel="stylesheet">
<style>
  :root {
    --canvas-bg: #e9eaec;
    --teal-deep: #3f7fa6;
    --teal-mid: #3aa9cf;
    --cyan-bright: #46c6e2;
    --sky-pale: #d8eef8;
    --white: #ffffff;
    --ink: #1b1b1d;
    --suit-dark: #2a2d33;
    --suit-mid: #4a4f58;
  }
  * { margin: 0; padding: 0; box-sizing: border-box; }
  html, body {
    width: 1200px; height: 900px; overflow: hidden;
    background: var(--canvas-bg);
  }
  .sign-poster {
    position: absolute;
    left: 300px; top: 40px;
    width: 600px; height: 820px;
    overflow: hidden;
    background:
      radial-gradient(ellipse 60% 40% at 75% 10%, rgba(90,210,230,.75), transparent 70%),
      linear-gradient(168deg, var(--teal-deep) 0%, var(--teal-mid) 30%, var(--cyan-bright) 55%, var(--sky-pale) 78%, var(--white) 100%);
  }
  .program-label {
    position: absolute; left: 52px; top: 82px;
    font-family: "Raleway", sans-serif; font-weight: 400;
    font-size: 21px; line-height: 1.3; letter-spacing: -0.3px;
    color: var(--white); text-transform: uppercase;
  }
  .challenge-headline {
    position: absolute; left: 58px; top: 150px;
    font-family: "Fredoka", sans-serif; font-weight: 700;
    font-size: 78px; line-height: 1.06; letter-spacing: -2px;
    color: var(--white); text-transform: uppercase;
  }
  .challenge-headline span { display: block; }
  .challenge-headline .line-2 { padding-left: 12px; }
  .challenge-headline .line-3 { padding-left: 24px; }
  .challenge-headline .line-4 { padding-left: 36px; }
  .doctor-portrait {
    position: absolute; right: 0; bottom: 0;
    width: 172px; height: 480px;
    background: linear-gradient(180deg, rgba(74,79,88,.3) 0%, var(--suit-mid) 35%, var(--suit-dark) 100%);
    border-top-left-radius: 90px 70px;
  }
  .clinic-brand {
    position: absolute; left: 110px; top: 640px;
    display: flex; align-items: center; gap: 12px;
    font-family: "Fredoka", sans-serif; font-weight: 600;
    color: var(--ink); text-transform: uppercase;
  }
  .clinic-brand .brand-dot {
    width: 30px; height: 30px; border-radius: 50%;
    background: var(--ink);
  }
  .clinic-brand .brand-name { display: flex; flex-direction: column; line-height: 1.1; }
  .clinic-brand .brand-name-main { font-size: 26px; }
  .clinic-brand .brand-name-sub { font-size: 15px; }
  .clinic-phone {
    position: absolute; left: 90px; top: 728px;
    display: flex; align-items: center; gap: 10px;
    font-family: "Fredoka", sans-serif; font-weight: 700;
    font-size: 34px; color: var(--ink);
  }
  .clinic-phone svg { width: 34px; height: 40px; }
</style>
</head>
<body>
  <main class="sign-poster">
    <p class="program-label">Dr. Halvorsen'<br>Weight Loss Program</p>
    <h1 class="challenge-headline">
      <span class="line-1">Lose up to</span>
      <span class="line-2">1 Pound</span>
      <span class="line-3">of fat</span>
      <span class="line-4">per day</span>
    </h1>
    <div class="doctor-portrait" role="img" aria-label="Photo of the doctor in a dark suit and teal tie"></div>
    <div class="clinic-brand">
      <span class="brand-dot"></span>
      <span class="brand-name">
        <span class="brand-name-main">Meridian</span>
        <span class="brand-name-sub">Wellness Clinics</span>
      </span>
    </div>
    <div class="clinic-phone">
      <svg viewBox="0 0 38 44" aria-hidden="true">
        <path d="M8 4c2-1 4 0 5 2l3 7c1 2 0 3-1 4l-3 2c1 5 4 10 8 13l3-2c1-1 3-1 4 0l5 5c1 2 1 3 0 5l-3 2c-3 2-8 1-13-4C9 32 4 22 4 14c0-5 2-8 4-10z" fill="#1b1b1d"/>
        <path d="M22 10a8 8 0 0 1 7 8M23 4a14 14 0 0 1 12 13" fill="none" stroke="#1b1b1d" stroke-width="2.5" stroke-linecap="round"/>
      </svg>
      <span>555-206–3948</span>
    </div>
  </main>
</body>
</html>
```